Lakeshore Vision Associates, P.C.
Diseases and Surgeries of the Retina, Macula and Vitreous
Lakeshore Vision Associates, P.C. - Medical
Creative Brief
Professional
Peter R. Haldane, MD
Birchwood Medical Tower 4215 N. Lindon Suite 812 Wexmore, IL 60952
peter@lakeshorevsa.com
www.lakeshorevsa.com
Appointment Date: MM/DD/YYYY at ____________am ___________pm Please telephone in advance if you will be unable to keep the appointment

```html
<!DOCTYPE html>
<html lang="en">
<head>
<meta charset="utf-8">
<title>Lakeshore Vision Associates – Stationery</title>
<link rel="stylesheet" href="https://fonts.googleapis.com/css2?family=Lato:wght@400;700&display=swap">
<style>
  :root {
    --stage: #e4e1dd;
    --paper: #ffffff;
    --ink: #333333;
    --muted: #8a8a8a;
    --rule: #cfcfcf;
    --orange: #f07a1a;
    --orange-deep: #d9530f;
    --band-dark: #3a3a3a;
    --faint: #f3e6da;
  }
  * { box-sizing: border-box; margin: 0; padding: 0; }
  html, body { width: 1200px; height: 576px; overflow: hidden; }
  body {
    background: var(--stage);
    font-family: "Lato", sans-serif;
    color: var(--ink);
    position: relative;
  }
  .sheet {
    position: absolute;
    background: var(--paper);
    box-shadow: 0 2px 6px rgba(0,0,0,.18);
    overflow: hidden;
  }

  /* brand lockup */
  .brand { position: absolute; display: flex; align-items: center; gap: 4px; }
  .brand-dot { border-radius: 50%; background: var(--orange); flex: none; }
  .brand-name {
    color: var(--ink); font-weight: 700; letter-spacing: .08em;
    text-transform: uppercase; line-height: 1.05;
  }

  .watermark {
    position: absolute; border-radius: 50%;
    background: radial-gradient(circle, #f6e4d2 0%, #fbf1e8 55%, #f2f2f2 100%);
    border: 2px solid #ececec;
  }

  /* footer band */
  .footer-band {
    position: absolute; left: 0; right: 0; height: 3px;
    background: linear-gradient(90deg, var(--orange) 0 18%, var(--band-dark) 18% 40%, #bdbdbd 100%);
  }
  .footer-text { position: absolute; font-size: 3.4px; color: var(--muted); line-height: 1.4; }
  .footer-text strong { color: var(--ink); font-weight: 700; }

  /* letterhead + fax */
  .letterhead { left: 96px; top: 108px; width: 240px; height: 312px; }
  .fax { left: 384px; top: 108px; width: 240px; height: 312px; }
  .fax-title { position: absolute; left: 14px; top: 66px; font-size: 15px; font-weight: 700; }
  .fax-fields { position: absolute; left: 14px; top: 90px; width: 212px; display: grid; grid-template-columns: 1fr 1fr; column-gap: 14px; row-gap: 6px; }
  .fax-field { font-size: 4px; color: var(--muted); border-bottom: 1px solid var(--rule); height: 8px; }
  .fax-checks { position: absolute; left: 14px; top: 146px; display: flex; gap: 9px; font-size: 3.6px; color: var(--muted); }
  .fax-check { display: flex; align-items: center; gap: 2px; }
  .fax-check i { width: 5px; height: 5px; border: 0.6px solid var(--muted); display: inline-block; }

  /* envelopes */
  .envelope-back { left: 720px; top: 96px; width: 396px; height: 168px; }
  .envelope-front { left: 720px; top: 276px; width: 396px; height: 132px; }
  .return-address { position: absolute; left: 58px; top: 30px; font-size: 4px; color: var(--muted); line-height: 1.5; }
  .envelope-web { position: absolute; left: 14px; bottom: 2px; font-size: 3.8px; color: var(--muted); }

  /* cards */
  .card { width: 150px; height: 84px; top: 444px; }
  .card-business { left: 780px; }
  .card-appointment { left: 946px; }
  .card-name { position: absolute; left: 10px; top: 34px; font-size: 6px; font-weight: 700; }
  .card-role { position: absolute; left: 10px; top: 42px; font-size: 3.6px; color: var(--muted); }
  .card-contact { position: absolute; left: 10px; top: 52px; font-size: 3.4px; color: var(--muted); line-height: 1.5; }
  .appt-title { position: absolute; left: 10px; top: 10px; font-size: 4.4px; font-weight: 700; }
  .appt-line { position: absolute; left: 10px; top: 22px; width: 130px; font-size: 3.8px; color: var(--muted); line-height: 2.1; }
  .appt-note { position: absolute; left: 10px; top: 50px; width: 90px; font-size: 3.2px; color: var(--muted); }
</style>
</head>
<body>

<!-- Letterhead -->
<section class="sheet letterhead">
  <div class="brand" style="left:12px;top:12px;">
    <span class="brand-dot" style="width:14px;height:14px;"></span>
    <span class="brand-name" style="font-size:5.4px;">Lakeshore<br>Vision Associates</span>
  </div>
  <div class="watermark" style="left:70px;top:110px;width:100px;height:100px;"></div>
  <div class="footer-band" style="bottom:26px;"></div>
  <p class="footer-text" style="left:12px;bottom:12px;">
    <strong>Lakeshore Vision Associates, P.C.</strong> · Diseases and Surgeries of the Retina, Macula and Vitreous<br>
    Birchwood Medical Tower · 4215 N. Lindon Suite 812 · Wexmore, IL 60952 · T 312.555.0190 · F 312.555.0191
  </p>
</section>

<!-- Fax cover -->
<section class="sheet fax">
  <div class="brand" style="left:12px;top:12px;">
    <span class="brand-dot" style="width:14px;height:14px;"></span>
    <span class="brand-name" style="font-size:5.4px;">Lakeshore<br>Vision Associates</span>
  </div>
  <h1 class="fax-title">FAX</h1>
  <div class="fax-fields">
    <div class="fax-field">To:</div><div class="fax-field">Date:</div>
    <div class="fax-field">Fax:</div><div class="fax-field">Pages:</div>
    <div class="fax-field">Phone:</div><div class="fax-field">CC:</div>
    <div class="fax-field">Re:</div><div class="fax-field">From:</div>
  </div>
  <div class="fax-checks">
    <span class="fax-check"><i></i>Urgent</span>
    <span class="fax-check"><i></i>For Review</span>
    <span class="fax-check"><i></i>Please Comment</span>
    <span class="fax-check"><i></i>Please Reply</span>
    <span class="fax-check"><i></i>Please Recycle</span>
  </div>
  <div class="footer-band" style="bottom:26px;"></div>
  <p class="footer-text" style="left:12px;bottom:12px;">
    <strong>Lakeshore Vision Associates, P.C.</strong> · Diseases and Surgeries of the Retina, Macula and Vitreous<br>
    Birchwood Medical Tower · 4215 N. Lindon Suite 812 · Wexmore, IL 60952 · T 312.555.0190 · F 312.555.0191
  </p>
</section>

<!-- Envelope back with flap -->
<section class="sheet envelope-back">
  <svg width="396" height="168" viewBox="0 0 396 168" style="position:absolute;left:0;top:0;">
    <defs>
      <linearGradient id="flap-fill" x1="0" y1="0" x2="0" y2="1">
        <stop offset="0" stop-color="var(--orange-deep)"/>
        <stop offset="1" stop-color="var(--orange)"/>
      </linearGradient>
    </defs>
    <path d="M0 168 L150 90 M396 168 L246 90" stroke="#e3e3e3" stroke-width="1" fill="none"/>
    <polygon points="0,0 396,0 198,60" fill="url(#flap-fill)"/>
    <polygon points="0,0 396,0 198,60" fill="none" stroke="#e8e8e8"/>
    <circle cx="198" cy="52" r="9" fill="#f4f4f4"/>
    <circle cx="198" cy="52" r="6" fill="var(--orange)"/>
  </svg>
</section>

<!-- Envelope front -->
<section class="sheet envelope-front">
  <div class="brand" style="left:14px;top:12px;">
    <span class="brand-dot" style="width:12px;height:12px;"></span>
    <span class="brand-name" style="font-size:4.8px;">Lakeshore<br>Vision Associates</span>
  </div>
  <p class="return-address">Birchwood Medical Tower<br>4215 N. Lindon Suite 812<br>Wexmore, IL 60952</p>
  <div class="watermark" style="right:22px;top:52px;width:52px;height:52px;"></div>
  <div class="footer-band" style="bottom:10px;"></div>
  <p class="envelope-web">www.lakeshorevsa.com</p>
</section>

<!-- Business card -->
<section class="sheet card card-business">
  <div class="brand" style="left:10px;top:10px;">
    <span class="brand-dot" style="width:10px;height:10px;"></span>
    <span class="brand-name" style="font-size:4px;">Lakeshore<br>Vision Associates</span>
  </div>
  <p class="card-name">Peter R. Haldane, MD</p>
  <p class="card-role">Diseases and Surgeries of the Retina, Macula and Vitreous</p>
  <p class="card-contact">Birchwood Medical Tower · 4215 N. Lindon Suite 812<br>Wexmore, IL 60952 · T 312.555.0190<br>peter@lakeshorevsa.com · www.lakeshorevsa.com</p>
  <div class="footer-band" style="bottom:4px;"></div>
</section>

<!-- Appointment card -->
<section class="sheet card card-appointment">
  <p class="appt-title">Appointment Date:</p>
  <p class="appt-line">MM/DD/YYYY at ____________am ___________pm</p>
  <p class="appt-note">Please telephone in advance if you will be unable to keep the appointment</p>
  <div class="brand" style="right:10px;top:56px;">
    <span class="brand-dot" style="width:8px;height:8px;"></span>
    <span class="brand-name" style="font-size:3.4px;">Lakeshore<br>Vision Associates</span>
  </div>
  <div class="footer-band" style="bottom:4px;"></div>
</section>

</body>
</html>
```